Web design for an intellectual property law practice

I need to design a simple landing page that may in the future expand to a full site. It should be very high tech focused.

Target Market(s)

Anyone seeking legal services

Industry/Entity Type

Legal

Number of Pages Required

2 page

Font styles to use
Other font styles liked:
• The same font as my logo

Colors
ec1f27

Requirements
Must have
• My logo (see attached).
Nice to have
• Open to ideas.

```html
<!DOCTYPE html>
<html lang="en">
<head>
<meta charset="utf-8">
<title>Northfield Patent Law</title>
<link href="https://fonts.googleapis.com/css2?family=Lato:wght@300;400;700;900&display=swap" rel="stylesheet">
<style>
:root{
  --red:#ec1f27;
  --ink:#1d1d1d;
  --dark:#202225;
  --grey:#555;
  --light:#eeeeee;
  --white:#ffffff;
}
*{margin:0;padding:0;box-sizing:border-box}
html,body{width:1200px;height:3814px;overflow:hidden;background:var(--white)}
body{font-family:'Lato',sans-serif;color:var(--ink);position:relative}
.abs{position:absolute}

/* hero */
.hero{left:0;top:0;width:1200px;height:900px;background:linear-gradient(120deg,#2b2d30 0%,#4a4643 40%,#6b5c4c 70%,#3a3632 100%)}
.brand{left:114px;top:118px;color:var(--white);font-size:26px;font-weight:700;letter-spacing:0.5px}
.brand-dot{left:186px;top:34px;width:62px;height:62px;border:3px solid var(--white);border-radius:50%}
.call{right:112px;top:52px;color:var(--white);font-size:19px;font-weight:700;display:flex;align-items:center;gap:14px}
.call .ico{width:36px;height:36px;border-radius:50%;background:var(--red);display:flex;align-items:center;justify-content:center}
.nav{left:526px;top:114px;display:flex;gap:44px;color:var(--white);font-size:15px;font-weight:700;align-items:center}
.hero-title{left:0;top:270px;width:1200px;text-align:center;color:var(--white);font-size:88px;font-weight:900;line-height:94px;letter-spacing:1px}
.hero-sub{left:220px;top:470px;width:760px;text-align:center;color:var(--white);font-size:17px;font-weight:700;line-height:32px}
.hero-btn{left:432px;top:567px;width:336px;height:63px;background:var(--red);color:var(--white);font-size:33px;font-weight:700;display:flex;align-items:center;justify-content:center;gap:14px}
.arrows{left:830px;top:790px;display:flex;gap:10px}
.arrows span{width:44px;height:44px;border-radius:50%;background:rgba(0,0,0,.55);display:flex;align-items:center;justify-content:center}

/* about */
.portrait{left:0;top:712px;width:508px;height:790px;background:radial-gradient(ellipse at 50% 30%,#c9a792 0%,#8a7468 28%,#2c2f36 60%,#1b1d22 100%)}
.eyebrow{left:590px;top:935px;color:var(--red);font-size:15px}
.about-title{left:590px;top:968px;font-size:50px;font-weight:400;letter-spacing:1px}
.about-text{left:590px;top:1052px;width:500px;color:var(--grey);font-size:13px;line-height:30px}
.about-text u{color:var(--ink)}
.btn-red{background:var(--red);color:var(--white);font-size:13px;font-weight:700;display:flex;align-items:center;justify-content:center}
.about-btn{left:590px;top:1342px;width:165px;height:51px}
.side-word{color:#ececec;font-weight:900;font-size:88px;letter-spacing:4px;transform-origin:left top;transform:rotate(-90deg);white-space:nowrap}
.side-about{left:1125px;top:1455px}

/* experience */
.experience{left:0;top:1502px;width:1200px;height:985px;background:linear-gradient(180deg,#f6f6f6 0%,#e7e7e7 60%,#ededed 100%)}
.ghost{left:0;top:1605px;width:1200px;text-align:center;color:rgba(0,0,0,.07);font-size:82px;font-weight:900;letter-spacing:6px;padding-left:0}
.exp-title{left:0;top:1645px;width:1200px;text-align:center;font-size:42px;font-weight:400;letter-spacing:1px}
.svc-text{width:260px;text-align:center;color:var(--grey);font-size:13px;line-height:24px}
.btn-outline{border:2px solid var(--red);color:var(--ink);font-size:13px;font-weight:700;display:flex;align-items:center;justify-content:center;width:137px;height:38px;background:var(--white)}

/* video */
.video-band{left:0;top:2487px;width:1200px;height:1267px;background:linear-gradient(180deg,#d9d6d3 0%,#ece9e6 40%,#f2f0ee 100%)}
.video-title{left:0;top:2618px;width:1200px;text-align:center;color:var(--white);font-size:42px;font-weight:700;letter-spacing:1px}
.video-title b{color:var(--red);font-weight:700}
.video-card{left:272px;top:2728px;width:656px;height:343px;background:linear-gradient(135deg,#f3f3f1 0%,#d7ddd8 45%,#5f8e87 70%,#e9e9e7 100%);box-shadow:0 8px 20px rgba(0,0,0,.25)}
.video-bar{left:272px;top:3020px;width:656px;height:51px;background:var(--red);color:var(--white);font-size:24px;font-weight:700;display:flex;align-items:center;justify-content:center}
.play{left:562px;top:2862px;width:76px;height:76px;border-radius:50%;background:rgba(30,30,30,.85);border:3px solid var(--white);display:flex;align-items:center;justify-content:center}

/* contact */
.contact-mark{left:558px;top:3166px;width:84px;height:84px;border-radius:50%;background:var(--white);box-shadow:0 2px 8px rgba(0,0,0,.15)}
.q-title{left:0;top:3318px;width:1200px;text-align:center;font-size:34px;font-weight:700;letter-spacing:1px}
.q-sub{left:0;top:3380px;width:1200px;text-align:center;font-size:17px}
.q-name{left:0;top:3426px;width:1200px;text-align:center;font-size:17px;color:var(--red)}
.q-phone{left:0;top:3468px;width:1200px;text-align:center;font-size:26px;font-weight:700}
.q-btn{left:498px;top:3544px;width:204px;height:46px}
.social{left:470px;top:3640px;display:flex;gap:7px}
.social span{width:60px;height:60px;border-radius:50%;background:#3a3a3a}
.side-contact{left:70px;top:3754px;color:rgba(0,0,0,.08)}

/* footer */
.footer{left:0;top:3754px;width:1200px;height:60px;background:#1a1a1a;color:var(--white);font-size:13px;display:flex;align-items:center;justify-content:space-between;padding:0 110px}
.footer nav{display:flex;gap:10px}
</style>
</head>
<body>

<!-- hero -->
<div class="abs hero" role="img" aria-label="Photo of a lawyer working at a desk with law books"></div>
<div class="abs brand-dot" aria-hidden="true"></div>
<div class="abs brand">northfieldpatentlaw</div>
<div class="abs call"><span class="ico"><svg width="18" height="18" viewBox="0 0 24 24"><path fill="#fff" d="M6.6 10.8a15.1 15.1 0 0 0 6.6 6.6l2.2-2.2c.3-.3.7-.4 1-.2 1.1.4 2.3.6 3.6.6.6 0 1 .4 1 1V20c0 .6-.4 1-1 1A17 17 0 0 1 3 4c0-.6.4-1 1-1h3.5c.6 0 1 .4 1 1 0 1.3.2 2.5.6 3.6.1.3 0 .7-.2 1z"/></svg></span>CALL US : (416) 555-0187</div>
<nav class="abs nav"><span>HOME</span><span>ABOUT US</span><span>SERVICES</span><span>BLOG</span><span>CONTACT US</span>
<svg width="16" height="16" viewBox="0 0 24 24"><circle cx="10" cy="10" r="7" fill="none" stroke="#fff" stroke-width="3"/><line x1="15" y1="15" x2="22" y2="22" stroke="#fff" stroke-width="3"/></svg></nav>
<h1 class="abs hero-title">CANADIAN PATENT<br>LAWYER</h1>
<p class="abs hero-sub">Daniel R. Whitcombe is a patent lawyer with expertise in the acquisition, protection &amp; enforcement of intellectual property in Canada. Helping you with your Canadian IP rights.</p>
<div class="abs hero-btn"><svg width="30" height="30" viewBox="0 0 24 24"><path fill="#fff" d="M6.6 10.8a15.1 15.1 0 0 0 6.6 6.6l2.2-2.2c.3-.3.7-.4 1-.2 1.1.4 2.3.6 3.6.6.6 0 1 .4 1 1V20c0 .6-.4 1-1 1A17 17 0 0 1 3 4c0-.6.4-1 1-1h3.5c.6 0 1 .4 1 1 0 1.3.2 2.5.6 3.6.1.3 0 .7-.2 1z"/></svg>(416) 555-0187</div>

<svg class="abs" style="left:0;top:640px" width="1200" height="270" viewBox="0 0 1200 270" aria-hidden="true">
  <path d="M0 125 C150 40 330 20 470 45 C700 90 900 230 1200 130 L1200 270 L0 270 Z" fill="#fff"/>
  <path d="M0 125 C150 40 330 20 470 45 C700 90 900 230 1200 130" fill="none" stroke="#ec1f27" stroke-width="6"/>
  <path d="M0 122 C150 38 330 18 470 43" fill="none" stroke="#ec1f27" stroke-width="10"/>
</svg>
<div class="abs arrows"><span><svg width="14" height="14" viewBox="0 0 24 24"><path d="M16 3 7 12l9 9" fill="none" stroke="#fff" stroke-width="3"/></svg></span><span><svg width="14" height="14" viewBox="0 0 24 24"><path d="m8 3 9 9-9 9" fill="none" stroke="#fff" stroke-width="3"/></svg></span></div>

<!-- about -->
<div class="abs portrait" role="img" aria-label="Portrait photo of the patent lawyer in a dark suit"></div>
<div class="abs side-word side-about">ABOUT</div>
<div class="abs eyebrow">Biography</div>
<h2 class="abs about-title">ABOUT ME</h2>
<p class="abs about-text"><u>DANIEL R. WHITCOMBE</u> is a partner with HARTLEY in its Toronto Office. Daniel is an intellectual property lawyer with the firm's Technology and Intellectual Property practice groups. Daniel's practice focuses on all aspects of the acquisition, protection, enforcement and strategic use of a wide range of intellectual property assets in Canada and around the world.<br>Daniel acts for a range of clients, from individual inventors, start-ups and other early stage companies to large multinational companies, and is actively involved in counselling clients and providing strategic advice in a variety..</p>
<div class="abs btn-red about-btn">READ MORE INFO</div>

<!-- experience -->
<div class="abs experience" role="img" aria-label="Faded background photo of an office desk"></div>
<div class="abs ghost">SERVICES</div>
<h2 class="abs exp-title">EXPERIENCE</h2>

<svg class="abs" style="left:0;top:1740px" width="1200" height="460" viewBox="0 0 1200 460" aria-label="Service tiles with photos of hands, a businesswoman and a pen signing" role="img">
  <defs>
    <linearGradient id="g1" x1="0" y1="0" x2="1" y2="1"><stop offset="0" stop-color="#e9e4df"/><stop offset="1" stop-color="#b6a79a"/></linearGradient>
    <linearGradient id="g2" x1="0" y1="0" x2="1" y2="1"><stop offset="0" stop-color="#dfe3e8"/><stop offset="1" stop-color="#7d8692"/></linearGradient>
    <linearGradient id="g3" x1="0" y1="0" x2="1" y2="1"><stop offset="0" stop-color="#d6d1cc"/><stop offset="1" stop-color="#6d625a"/></linearGradient>
  </defs>
  <!-- left -->
  <path d="M280 60 L445 225 L280 390 L115 225 Z" fill="url(#g1)"/>
  <path d="M180 290 L380 290 L280 390 Z" fill="#1f1f1f"/>
  <text x="280" y="332" text-anchor="middle" fill="#fff" font-family="Lato,sans-serif" font-size="15">Trademark</text>
  <text x="280" y="352" text-anchor="middle" fill="#fff" font-family="Lato,sans-serif" font-size="15">Protection</text>
  <!-- right -->
  <path d="M920 60 L1085 225 L920 390 L755 225 Z" fill="url(#g3)"/>
  <path d="M820 290 L1020 290 L920 390 Z" fill="#1f1f1f"/>
  <text x="920" y="316" text-anchor="middle" fill="#fff" font-family="Lato,sans-serif" font-size="15">Commercial</text>
  <text x="920" y="336" text-anchor="middle" fill="#fff" font-family="Lato,sans-serif" font-size="15">Intellectual</text>
  <text x="920" y="356" text-anchor="middle" fill="#fff" font-family="Lato,sans-serif" font-size="15">Property</text>
  <!-- center -->
  <path d="M600 25 L805 230 L600 435 L395 230 Z" fill="#fff"/>
  <path d="M600 35 L795 230 L600 425 L405 230 Z" fill="url(#g2)"/>
  <path d="M475 300 L725 300 L600 425 Z" fill="#ec1f27"/>
  <text x="600" y="348" text-anchor="middle" fill="#fff" font-family="Lato,sans-serif" font-size="17">Patents &amp; Industrial</text>
  <text x="600" y="372" text-anchor="middle" fill="#fff" font-family="Lato,sans-serif" font-size="17">Designs</text>
</svg>

<p class="abs svc-text" style="left:150px;top:2192px">As a registered trademark agent, Daniel advises local, national and international clients on how to efficiently and effectively conduct</p>
<p class="abs svc-text" style="left:460px;top:2192px;width:280px">As a registered patent agent with the Canadian Intellectual Property Office (CIPO), Daniel's practice focuses on the drafting and prosecuting of patent applications in Canada</p>
<p class="abs svc-text" style="left:790px;top:2192px">Daniel is frequently called upon to advise clients on commercializing intellectual property rights, including technology acquisition &amp; licensing.</p>
<div class="abs btn-outline" style="left:213px;top:2328px">READ MORE</div>
<div class="abs btn-outline" style="left:531px;top:2328px">READ MORE</div>
<div class="abs btn-outline" style="left:849px;top:2328px">READ MORE</div>

<!-- video -->
<div class="abs video-band" role="img" aria-label="Faded photo of a team meeting behind the contact area"></div>
<svg class="abs" style="left:0;top:2487px" width="1200" height="300" viewBox="0 0 1200 300" role="img" aria-label="City skyline at dusk">
  <defs><linearGradient id="sky" x1="0" y1="0" x2="0" y2="1"><stop offset="0" stop-color="#2a2a2c"/><stop offset=".7" stop-color="#4a3f36"/><stop offset="1" stop-color="#1c1c1e"/></linearGradient></defs>
  <path d="M0 0 H1200 V130 L0 290 Z" fill="url(#sky)"/>
</svg>
<div class="abs ghost" style="top:2580px;color:rgba(255,255,255,.08)">WATCH VIDEO</div>
<h2 class="abs video-title"><b>FAQ</b> VIDEO</h2>
<div class="abs video-card" role="img" aria-label="Video still of patent technical drawings with IP category tiles"></div>
<div class="abs play"><svg width="28" height="30" viewBox="0 0 28 30"><path d="M4 2 L26 15 L4 28 Z" fill="#fff"/></svg></div>
<div class="abs video-bar">Why IP Matters to Your StartUp</div>

<!-- contact -->
<div class="abs contact-mark" aria-hidden="true"></div>
<div class="abs side-word side-contact">CONTACT</div>
<h2 class="abs q-title">QUESTIONS?</h2>
<p class="abs q-sub">Don't hesitate to reach out if you have any questions</p>
<p class="abs q-name">Northfield Patent Law</p>
<p class="abs q-phone">(416) 555-0187</p>
<div class="abs btn-red q-btn">SEND ME AN EMAIL</div>
<div class="abs social"><span aria-label="Social link"></span><span aria-label="Social link"></span><span aria-label="Social link"></span><span aria-label="Social link"></span></div>

<!-- footer -->
<footer class="abs footer"><span>Copyright © 2019 Northfield Patent Law - All Rights Reserved.</span><nav><span>Privacy policy</span><span>|</span><span>Terms and Use</span></nav></footer>

</body>
</html>
```